Tidewell HVAC WordPress website design

Design a new modern, clean, website for HVAC mechanical business that uses company logo/colors for branding and recognition. Files attached are just for band and color information. Here is a website design that appeals to me https://www.quillerbyhomes.example/

A clear description of who we are and what we do

An easily-navigated site map

An easily-navigated site map for mobile devices

Easy-to-find contact information

Obvious call to action for service, installs or to schedule estimates

about us page

Provide a way for potential customers to contact us via text or email

provide a way that allows a customer to upload a picture to request a service call or quote.
Updates

I'm looking for the design to be completed in WordPress

Industry/Entity Type

HVAC Mechanical & Building Automation / Controls contractor

Coding

Coded - Design and coding required

Number of Pages Required

5+ page

Colors
0054AA
0677BA
7BADD7
CADEEF
E8F1F8

Requirements
Must have
• Design a new modern, clean, website for HVAC mechanical business that uses company logo/colors for branding and recognition. Files attached are just for band and color information. Here is a website design that appeals to me https://www.quillerbyhomes.example/ A clear description of who we are and what we do An easily-navigated site map An easily-navigated site map for mobile devices Easy-to-find contact information Obvious call to action for service, installs or to schedule estimates about us page Provide a way for potential customers to contact us via text or email provide a way that allows a customer to upload a picture to request a service call or quote.
Nice to have

```html
<!DOCTYPE html>
<html lang="en">
<head>
<meta charset="utf-8">
<title>Tidewell HVAC</title>
<link href="https://fonts.googleapis.com/css2?family=Josefin+Sans:wght@400;600;700&family=Montserrat:wght@400;500;600;700&family=Hind:wght@500;600&display=swap" rel="stylesheet">
<style>
:root{
  --navy:#0a3a78;
  --brand:#0054AA;
  --mid:#0677BA;
  --sky:#7BADD7;
  --pale:#CADEEF;
  --mist:#E8F1F8;
  --ink:#1a1a1a;
  --grey:#444;
  --white:#fff;
  --black:#050505;
}
*{margin:0;padding:0;box-sizing:border-box}
html,body{width:1200px;height:4444px;overflow:hidden}
body{position:relative;background:var(--white);font-family:"Montserrat",sans-serif;color:var(--ink)}
.abs{position:absolute}
.head{font-family:"Josefin Sans",sans-serif}
.btn{position:absolute;display:flex;align-items:center;justify-content:center;border-radius:20px;background:var(--navy);color:var(--white);font-weight:700;font-size:12px;letter-spacing:1px}
.photo{position:absolute}

/* top bar & nav */
.topbar{left:0;top:0;width:1200px;height:64px;background:linear-gradient(90deg,var(--navy),var(--brand));color:var(--white);font-size:12px;font-weight:700;letter-spacing:1px}
.topbar span{position:absolute;top:27px}
.topbar svg{position:absolute;top:19px}
.brand{left:112px;top:80px;display:flex;align-items:center;gap:10px}
.brand-dot{width:34px;height:34px;border-radius:50%;background:var(--brand)}
.brand-name{font-family:"Montserrat",sans-serif;font-weight:700;font-size:21px;color:var(--brand);letter-spacing:.5px}
.nav a{position:absolute;top:99px;font-size:14px;color:var(--ink);text-decoration:none;letter-spacing:.5px}

/* hero */
.hero{left:0;top:150px;width:1200px;height:574px;background:linear-gradient(90deg,#1b2036 0%,#3b2a44 40%,#5a2a3a 60%,#2a4d8f 100%)}
.hero-welcome{left:114px;top:282px;font-size:30px;color:var(--white);letter-spacing:3px}
.hero-title{left:114px;top:330px;font-size:42px;color:var(--white);font-weight:600;letter-spacing:4px}
.hero-text{left:114px;top:393px;width:400px;font-size:11.5px;line-height:21px;color:var(--white);font-weight:600}

/* about */
.eyebrow{font-size:15px;letter-spacing:1px}
.about-title{left:645px;top:858px;font-size:36px;font-weight:600;letter-spacing:3px}
.about-text{left:647px;width:440px;font-size:11.5px;line-height:24px;color:var(--grey);letter-spacing:.5px}

/* works */
.works{left:0;top:1277px;width:1200px;height:460px;background:linear-gradient(180deg,var(--brand),var(--navy))}
.card{position:absolute;top:1457px;width:311px;height:310px;background:var(--white);box-shadow:0 4px 14px rgba(0,0,0,.12)}
.card .photo{left:9px;top:9px;width:293px;height:244px}
.card-label{position:absolute;left:20px;top:274px;font-size:14px;font-weight:600;letter-spacing:1px}
.card svg{position:absolute;right:18px;top:276px}

/* services */
.services-bg{left:0;top:1767px;width:1200px;height:620px;background:linear-gradient(180deg,#fff 0%,#eef3f8 40%,#dde7f1 80%,#fff 100%)}
.svc{position:absolute;top:1965px;width:240px;text-align:center}
.svc-label{margin-top:16px;font-size:13.5px;line-height:22px;letter-spacing:1.5px;color:#222}
.divider{position:absolute;top:1971px;width:0;height:172px;border-left:2px dashed #333}

/* stats */
.stat{color:var(--white);font-family:"Hind",sans-serif;font-weight:600;font-size:28px;line-height:31px}
.vline{position:absolute;top:2445px;width:3px;height:110px;background:var(--white)}

/* testimonial */
.testi-title{left:110px;top:2716px;font-family:"Hind",sans-serif;font-weight:600;font-size:34px}

/* quote */
.field{position:absolute;height:56px;border:2px solid var(--white);border-radius:28px;color:var(--white);font-size:13px;display:flex;align-items:center;padding-left:24px}

/* footer */
.footer{left:0;top:4060px;width:1200px;height:384px;background:var(--black);color:var(--white)}
.f-head{position:absolute;font-family:"Josefin Sans",sans-serif;font-weight:700;font-size:17px;letter-spacing:1.5px;color:var(--white)}
.f-link{position:absolute;font-size:13px;letter-spacing:1px;color:var(--white)}
.social{position:absolute;top:4305px;width:20px;height:20px;border-radius:3px}
</style>
</head>
<body>

<!-- top bar -->
<div class="abs topbar">
  <span style="left:373px">CONTACT US VIA TEXT OR EMAIL</span>
  <svg style="left:674px" width="28" height="28" viewBox="0 0 28 28"><circle cx="14" cy="14" r="13" fill="none" stroke="#fff" stroke-width="1.6"/><path d="M10 8l3 3-2 2c1 2 2 3 4 4l2-2 3 3-2 2c-5 0-10-5-10-10z" fill="#fff"/></svg>
  <span style="left:727px">555 · 013 · 4821</span>
  <svg style="left:892px" width="28" height="28" viewBox="0 0 28 28"><circle cx="14" cy="14" r="13" fill="none" stroke="#fff" stroke-width="1.6"/><rect x="8" y="9" width="12" height="10" rx="1" fill="none" stroke="#fff" stroke-width="1.6"/><path d="M8 10l6 5 6-5" fill="none" stroke="#fff" stroke-width="1.6"/></svg>
  <span style="left:951px">info@tidewellhvac.example</span>
</div>

<!-- nav -->
<div class="abs brand"><div class="brand-dot"></div><div class="brand-name">TIDEWELL HVAC</div></div>
<nav class="nav">
  <a style="left:524px">Home</a>
  <a style="left:620px">About Us</a>
  <a style="left:743px">Services</a>
  <a style="left:862px">Team</a>
</nav>
<div class="btn" style="left:955px;top:86px;width:133px;height:36px">Contact Us</div>

<!-- hero -->
<div class="abs hero" role="img" aria-label="Two HVAC technicians in hard hats and blue work uniforms standing in front of red industrial pipes and valves"></div>
<div class="abs hero-welcome head">Welcome To</div>
<div class="abs hero-title head">TIDEWELL HVAC</div>
<p class="abs hero-text">Lorem ipsum dolor sit amet, consectetur adipiscing elit, sed do eiusmod tempor incididunt ut labore et dolore magna aliqua.</p>
<div class="btn" style="left:114px;top:479px;width:200px;height:34px">Schedule an Service</div>

<!-- about -->
<div class="photo" style="left:112px;top:810px;width:250px;height:376px;border-radius:6px;background:linear-gradient(180deg,#e9e7e3,#c9b59a)" role="img" aria-label="Technician on a ladder servicing a wall-mounted air conditioner while a client watches"></div>
<div class="photo" style="left:367px;top:812px;width:236px;height:184px;border-radius:6px;background:linear-gradient(180deg,#cfd9e2,#6f8aa6)" role="img" aria-label="Technician cleaning the filter of an indoor air conditioning unit"></div>
<div class="photo" style="left:367px;top:1005px;width:236px;height:185px;border-radius:6px;background:linear-gradient(180deg,#8c8f94,#3c3f44)" role="img" aria-label="Technician working on an outdoor condenser unit"></div>
<div class="abs eyebrow" style="left:646px;top:832px">Who We Are?</div>
<div class="abs about-title head">About <span style="color:var(--brand)">Us</span></div>
<p class="abs about-text" style="top:912px">Lorem ipsum dolor sit amet, consectetur adipiscing elit, sed do eiusmod tempor incididunt ut labore et dolore magna aliqua. Ut enim ad minim veniam, quis nostrud exercitation ullamco laboris nisi ut aliquip ex ea commodo consequat.</p>
<p class="abs about-text" style="top:1019px">Duis aute irure dolor in reprehenderit in voluptate velit esse cillum dolore eu fugiat nulla pariatur. Excepteur sint occaecat cupidatat non proident, sunt in culpa qui officia deserunt mollit anim id est laborum.</p>
<div class="btn" style="left:643px;top:1134px;width:133px;height:35px">Read More</div>

<!-- what we do -->
<div class="abs works"></div>
<svg class="abs" style="left:0;top:1600px" width="1200" height="180" viewBox="0 0 1200 180"><path d="M0 125 Q600 -40 1200 125 L1200 180 L0 180 Z" fill="#fff"/></svg>
<div class="abs" style="left:0;top:1340px;width:1200px;text-align:center;color:#fff;font-size:14px;letter-spacing:1.5px">Our Works</div>
<div class="abs head" style="left:0;top:1366px;width:1200px;text-align:center;color:#fff;font-size:34px;font-weight:600;letter-spacing:3px">What We Do</div>

<div class="card" style="left:110px"><div class="photo" style="background:linear-gradient(135deg,#3a3c40,#b2453d)" role="img" aria-label="Technician in a plaid shirt adjusting a heating boiler control panel"></div><div class="card-label">Heating</div><svg width="18" height="14" viewBox="0 0 18 14"><path d="M1 7h15M11 2l5 5-5 5" fill="none" stroke="#0054AA" stroke-width="1.8"/></svg></div>
<div class="card" style="left:443px"><div class="photo" style="background:linear-gradient(180deg,#e3e5e8,#9aa0a8)" role="img" aria-label="Technician in a hard hat servicing a ceiling ventilation unit"></div><div class="card-label">Ventilation</div><svg width="18" height="14" viewBox="0 0 18 14"><path d="M1 7h15M11 2l5 5-5 5" fill="none" stroke="#0054AA" stroke-width="1.8"/></svg></div>
<div class="card" style="left:776px"><div class="photo" style="background:linear-gradient(180deg,#a8cdea,#d8c9a6)" role="img" aria-label="Technician in a cap repairing an outdoor air conditioning unit with a drill"></div><div class="card-label">Air Conditioning</div><svg width="18" height="14" viewBox="0 0 18 14"><path d="M1 7h15M11 2l5 5-5 5" fill="none" stroke="#0054AA" stroke-width="1.8"/></svg></div>

<!-- services -->
<div class="abs services-bg" role="img" aria-label="Faded background of a technician working on HVAC equipment"></div>
<div class="abs head" style="left:0;top:1848px;width:1200px;text-align:center;font-size:34px;font-weight:600;letter-spacing:3px">Our <span style="color:var(--brand)">Services</span></div>

<div class="svc" style="left:109px">
  <svg width="70" height="70" viewBox="0 0 70 70"><circle cx="35" cy="35" r="22" fill="none" stroke="#0054AA" stroke-width="9" stroke-dasharray="9 5"/><circle cx="35" cy="35" r="17" fill="#fff"/><path d="M25 35l8 8 18-20" fill="none" stroke="#0a3a78" stroke-width="6"/></svg>
  <div class="svc-label">INSTALLATION OF<br>HEATING, AIR<br>CONDITIONING,</div>
</div>
<div class="svc" style="left:368px">
  <svg width="70" height="70" viewBox="0 0 70 70"><circle cx="35" cy="35" r="24" fill="none" stroke="#0054AA" stroke-width="9" stroke-dasharray="9 5"/><circle cx="35" cy="35" r="13" fill="none" stroke="#0a3a78" stroke-width="5"/><path d="M35 35l9 9" stroke="#0a3a78" stroke-width="6"/></svg>
  <div class="svc-label">HEATING AND AIR<br>CONDITIONING<br>REPAIR</div>
</div>
<div class="svc" style="left:625px">
  <svg width="70" height="70" viewBox="0 0 70 70"><path d="M14 14l42 42M56 14L14 56" stroke="#0054AA" stroke-width="7" stroke-linecap="round"/><circle cx="15" cy="15" r="7" fill="#0a3a78"/><circle cx="55" cy="15" r="7" fill="#0a3a78"/></svg>
  <div class="svc-label">MAINTENANCE<br>SERVICES FOR HVAC<br>SYSTEMS</div>
</div>
<div class="svc" style="left:882px">
  <svg width="70" height="70" viewBox="0 0 70 70"><rect x="14" y="10" width="26" height="50" rx="3" fill="#0054AA"/><path d="M30 20l-8 14h8l-6 14 12-18h-8l6-10z" fill="#fff"/><path d="M40 40h8V20M44 12v8M52 12v8M43 20h10" fill="none" stroke="#0a3a78" stroke-width="4"/></svg>
  <div class="svc-label">ELECTRICAL<br>SERVICES</div>
</div>
<div class="divider" style="left:362px"></div>
<div class="divider" style="left:602px"></div>
<div class="divider" style="left:884px"></div>
<svg class="abs" style="left:220px;top:2127px" width="18" height="14" viewBox="0 0 18 14"><path d="M1 7h15M11 2l5 5-5 5" fill="none" stroke="#0054AA" stroke-width="1.8"/></svg>
<svg class="abs" style="left:479px;top:2127px" width="18" height="14" viewBox="0 0 18 14"><path d="M1 7h15M11 2l5 5-5 5" fill="none" stroke="#0054AA" stroke-width="1.8"/></svg>
<svg class="abs" style="left:736px;top:2127px" width="18" height="14" viewBox="0 0 18 14"><path d="M1 7h15M11 2l5 5-5 5" fill="none" stroke="#0054AA" stroke-width="1.8"/></svg>
<svg class="abs" style="left:993px;top:2127px" width="18" height="14" viewBox="0 0 18 14"><path d="M1 7h15M11 2l5 5-5 5" fill="none" stroke="#0054AA" stroke-width="1.8"/></svg>
<div class="btn" style="left:540px;top:2220px;width:120px;height:34px">View All</div>

<!-- stats -->
<svg class="abs" style="left:0;top:2328px" width="1200" height="326" viewBox="0 0 1200 326"><defs><linearGradient id="statsGrad" x1="0" y1="0" x2="0" y2="1"><stop offset="0" stop-color="#0054AA"/><stop offset="1" stop-color="#0a3a78"/></linearGradient></defs><path d="M0 100 Q600 -60 1200 100 L1200 326 L0 326 Z" fill="url(#statsGrad)"/></svg>
<div class="abs" style="left:152px;top:2458px;color:#fff;font-size:14px">Our Statistics</div>
<div class="abs stat" style="left:152px;top:2484px;font-size:32px;line-height:36px">Some Important<br>Facts</div>
<div class="abs stat" style="left:483px;top:2462px">10+ Years<br>Experience</div>
<div class="vline" style="left:651px"></div>
<div class="abs stat" style="left:717px;top:2460px">100+<br>Projects<br>Completed</div>
<div class="vline" style="left:897px"></div>
<div class="abs stat" style="left:972px;top:2460px">50+<br>Clients</div>

<!-- testimonial -->
<div class="photo" style="left:564px;top:2605px;width:636px;height:541px;background:linear-gradient(180deg,#7fb4e6 0%,#b9d4ea 40%,#3d5a7c 100%)" role="img" aria-label="Technician in a white hard hat and safety glasses wiring a rooftop HVAC unit"></div>
<div class="abs" style="left:0;top:2652px;width:660px;height:494px;background:#fff"></div>
<div class="abs" style="left:110px;top:2685px;font-size:14px">Testimonials</div>
<div class="abs testi-title">What Our <span style="color:var(--brand)">Client</span> says?</div>
<div class="abs" style="left:110px;top:2778px;font-family:Georgia,serif;font-size:44px;font-weight:700;color:var(--brand)">“</div>
<div class="photo" style="left:138px;top:2777px;width:90px;height:90px;border-radius:50%;background:linear-gradient(180deg,#d9c1a9,#f1ece7);box-shadow:0 2px 8px rgba(0,0,0,.15)" role="img" aria-label="Client portrait"></div>
<div class="abs" style="left:250px;top:2800px;font-size:15px">Marisol</div>
<div class="abs" style="left:249px;top:2820px;font-size:12px;color:#f2b01e;letter-spacing:1px">★★★★★</div>
<p class="abs" style="left:121px;top:2890px;width:350px;font-size:13px;line-height:27.5px;color:#222">Lorem ipsum dolor sit amet, consectetur adipiscing elit, sed do eiusmod tempor incididunt ut labore et dolore magna aliqua. Ut enim ad minim veniam, quis nostrud exercitation ullamco laboris nisi ut aliquip ex ea commodo consequat.</p>
<svg class="abs" style="left:118px;top:3055px" width="44" height="10" viewBox="0 0 44 10"><circle cx="5" cy="5" r="4" fill="#0054AA"/><circle cx="15" cy="5" r="3" fill="#bbb"/><circle cx="24" cy="5" r="3" fill="#bbb"/><circle cx="33" cy="5" r="3" fill="#bbb"/></svg>

<!-- quote -->
<div class="photo" style="left:0;top:3236px;width:471px;height:491px;background:linear-gradient(180deg,#c7d6e4,#6a4a3f)" role="img" aria-label="Two engineers in white hard hats reviewing plans beside industrial pipelines"></div>
<div class="abs" style="left:471px;top:3236px;width:729px;height:491px;background:linear-gradient(180deg,var(--navy),var(--brand))"></div>
<div class="abs" style="left:526px;top:3290px;color:#fff;font-family:'Hind',sans-serif;font-weight:600;font-size:34px">Request a Quote</div>
<div class="field" style="left:517px;top:3353px;width:262px">Name</div>
<div class="field" style="left:810px;top:3353px;width:262px">Phone</div>
<div class="field" style="left:519px;top:3422px;width:550px">Email</div>
<div class="field" style="left:519px;top:3489px;width:550px">Select Service
  <svg style="position:absolute;right:24px;top:22px" width="12" height="8" viewBox="0 0 12 8"><path d="M1 1l5 5 5-5" fill="none" stroke="#fff" stroke-width="1.5"/></svg></div>
<div class="field" style="left:519px;top:3557px;width:550px">Upload Picture
  <svg style="position:absolute;right:22px;top:16px" width="26" height="22" viewBox="0 0 26 22"><rect x="1" y="3" width="22" height="18" rx="2" fill="none" stroke="#fff" stroke-width="1.6"/><path d="M3 19l6-7 4 4 3-3 5 6z" fill="#fff"/><circle cx="16" cy="9" r="2" fill="#fff"/></svg></div>
<div class="btn" style="left:526px;top:3643px;width:133px;height:36px;background:#fff;color:#111">Submit</div>

<!-- newsletter -->
<div class="abs" style="left:0;top:3814px;width:1200px;text-align:center;font-size:16px;letter-spacing:1.5px">Newsletter Sign up</div>
<div class="abs head" style="left:0;top:3838px;width:1200px;text-align:center;font-size:35px;font-weight:600;letter-spacing:3px">Subscribe To <span style="color:var(--brand)">Our Newsletter</span></div>
<div class="abs" style="left:255px;top:3910px;width:688px;height:64px;border-radius:32px;background:#fff;box-shadow:0 3px 12px rgba(0,0,0,.15)"></div>
<div class="abs" style="left:303px;top:3935px;font-size:12px;letter-spacing:1px;color:#333">Enter Email Address</div>
<div class="abs" style="left:788px;top:3910px;width:155px;height:64px;border-radius:0 32px 32px 0;background:var(--navy);color:#fff;font-weight:700;font-size:13px;letter-spacing:1px;display:flex;align-items:center;justify-content:center">Subscribe</div>

<!-- footer -->
<div class="abs footer"></div>
<div class="abs" style="left:112px;top:4170px;display:flex;align-items:center;gap:10px"><div style="width:34px;height:34px;border-radius:50%;background:var(--brand)"></div><div class="brand-name" style="color:#fff">TIDEWELL HVAC</div></div>
<p class="abs" style="left:112px;top:4255px;width:218px;color:#fff;font-size:13px;line-height:22px;letter-spacing:1px">Lorem ipsum dolor sit amet, consectetur adipiscing elit, sed do eiusmod tempor incididunt.</p>

<div class="f-head" style="left:471px;top:4166px">Quick Links</div>
<div class="f-link" style="left:473px;top:4201px">Home</div>
<div class="f-link" style="left:473px;top:4231px">About Us</div>
<div class="f-link" style="left:473px;top:4261px">Services</div>
<div class="f-link" style="left:473px;top:4291px">Team</div>
<div class="f-link" style="left:473px;top:4321px">Contact Us</div>

<div class="f-head" style="left:651px;top:4166px">Help Links</div>
<div class="f-link" style="left:653px;top:4201px">Privacy Policy</div>
<div class="f-link" style="left:653px;top:4231px">Terms &amp; Conditions</div>
<div class="f-head" style="left:651px;top:4269px">Follow Us</div>
<div class="social" style="left:652px;background:#1f5bd6"></div>
<div class="social" style="left:677px;background:#fff"></div>
<div class="social" style="left:702px;background:#d0234b"></div>
<div class="social" style="left:727px;background:#c4368f"></div>
<div class="social" style="left:752px;background:#e52525"></div>

<div class="f-head" style="left:874px;top:4166px">Contact Us</div>
<svg class="abs" style="left:872px;top:4208px" width="26" height="26" viewBox="0 0 26 26"><circle cx="13" cy="13" r="12" fill="none" stroke="#fff" stroke-width="1.5"/><path d="M13 6a5 5 0 015 5c0 4-5 9-5 9s-5-5-5-9a5 5 0 015-5z" fill="#fff"/><circle cx="13" cy="11" r="2" fill="#050505"/></svg>
<div class="f-link" style="left:914px;top:4214px">Lorem Ipsum,Usa - 4379</div>
<svg class="abs" style="left:872px;top:4258px" width="26" height="26" viewBox="0 0 26 26"><circle cx="13" cy="13" r="12" fill="#fff"/><path d="M9 7l3 3-2 2c1 2 2 3 4 4l2-2 3 3-2 2c-5 0-10-5-10-10z" fill="#050505"/></svg>
<div class="f-link" style="left:914px;top:4264px">555 - 013 - 4821</div>
<svg class="abs" style="left:872px;top:4310px" width="26" height="26" viewBox="0 0 26 26"><circle cx="13" cy="13" r="12" fill="none" stroke="#fff" stroke-width="1.5"/><rect x="7" y="8" width="12" height="10" rx="1" fill="none" stroke="#fff" stroke-width="1.5"/><path d="M7 9l6 5 6-5" fill="none" stroke="#fff" stroke-width="1.5"/></svg>
<div class="f-link" style="left:914px;top:4316px">info@tidewellhvac.example</div>

<div class="abs" style="left:110px;top:4384px;width:980px;height:1px;background:#555"></div>
<div class="abs" style="left:0;top:4405px;width:1200px;text-align:center;color:#fff;font-size:11px;letter-spacing:1px">Copyright © 2024 Tidewell HVAC. All rights reserved.</div>

</body>
</html>
```